Bref créative
BrightHollow Capital Partners
......putting entrepreneurs and investors together
Professional
Marcus Pellow
418 Weldon Avenue
Suite 340
Larkmont, OH 44907
brighthollowcap@mailvista.net
I have selected the black & red color scheme on the logo.
Angel Investors/Angel Funds
Seed/Start-up Investment
Private Equity Funds
Venture Capital Funding
Merchant Funding
Receivable/Purchase Order Funding

```html
<!DOCTYPE html>
<html lang="en">
<head>
<meta charset="utf-8">
<title>BrightHollow Capital Partners – Business Cards</title>
<link rel="stylesheet" href="https://fonts.googleapis.com/css2?family=Arimo:wght@400;700&display=swap">
<style>
  :root {
    --page: #ececec;
    --card-border: #9a9a9a;
    --white: #ffffff;
    --ink: #222222;
    --black: #000000;
    --red: #c3121c;
    --red-deep: #7d0a10;
    --red-light: #d8222b;
  }
  * { box-sizing: border-box; margin: 0; padding: 0; }
  html, body { width: 1200px; height: 727px; overflow: hidden; }
  body {
    background: var(--page);
    font-family: "Arimo", Arial, sans-serif;
    position: relative;
  }
  .card {
    position: absolute;
    width: 567px;
    height: 329px;
    border: 2px solid var(--card-border);
    overflow: hidden;
  }
  .card--front { left: 19px; top: 19px; background: var(--white); }
  .card--back-red {
    left: 607px; top: 19px;
    background: radial-gradient(ellipse at 50% 40%, var(--red-light) 0%, var(--red) 45%, var(--red-deep) 100%);
  }
  .card--back-white { left: 19px; top: 367px; background: var(--white); }
  .card--back-black { left: 607px; top: 367px; background: var(--black); }

  .front-wave { position: absolute; left: 0; top: 0; width: 567px; height: 250px; }

  .contact {
    position: absolute;
    right: 24px; top: 30px;
    text-align: right;
    color: var(--white);
    font-size: 15px;
    line-height: 25px;
  }

  .brand {
    position: absolute;
    display: flex;
    align-items: center;
    gap: 10px;
    font-weight: 700;
    font-size: 25px;
    letter-spacing: 0.3px;
    white-space: nowrap;
  }
  .brand__dot {
    width: 14px; height: 14px;
    border-radius: 50%;
    background: var(--red);
    flex: none;
  }
  .brand--front { left: 26px; top: 262px; color: var(--ink); font-size: 22px; }
  .brand--centered { left: 0; right: 0; justify-content: center; top: 92px; }
  .brand--light { color: var(--white); }
  .brand--dark { color: var(--ink); }
  .card--back-red .brand__dot { background: var(--white); }

  .holder {
    position: absolute;
    left: 398px; top: 262px;
    color: var(--red);
    font-size: 20px;
  }

  .services {
    position: absolute;
    left: 0; right: 0; top: 186px;
    list-style: none;
    text-align: center;
    font-size: 15px;
    line-height: 22px;
  }
  .services--light { color: var(--white); }
  .services--dark { color: var(--ink); }
</style>
</head>
<body>

  <section class="card card--front">
    <svg class="front-wave" viewBox="0 0 567 250" aria-hidden="true">
      <defs>
        <linearGradient id="frontRed" x1="0" y1="0" x2="1" y2="1">
          <stop offset="0" stop-color="#7d0a10"/>
          <stop offset="0.5" stop-color="#c3121c"/>
          <stop offset="1" stop-color="#8e0b12"/>
        </linearGradient>
      </defs>
      <path d="M0,0 H567 V206 C480,220 400,186 300,182 C200,178 110,230 0,218 Z" fill="url(#frontRed)"/>
      <path d="M0,222 C110,234 200,182 300,186 C400,190 480,224 567,210" fill="none" stroke="#000" stroke-width="5"/>
      <path d="M0,230 C110,242 200,190 300,194 C400,198 480,232 567,218" fill="none" stroke="#bdbdbd" stroke-width="2"/>
    </svg>
    <div class="contact">
      418 Weldon Avenue<br>
      Suite 340, Larkmont, OH 44907<br>
      Cell: 330-555-0142 | Fax: 330-555-0179<br>
      Email: brighthollowcap@mailvista.net
    </div>
    <div class="brand brand--front"><span class="brand__dot"></span>BrightHollow Capital Partners</div>
    <div class="holder">Marcus Pellow</div>
  </section>

  <section class="card card--back-red">
    <div class="brand brand--centered brand--light"><span class="brand__dot"></span>BrightHollow Capital Partners</div>
    <ul class="services services--light">
      <li>Angel Investors/Angel Funds</li>
      <li>Seed/Start-up Investment</li>
      <li>Private Equity Funds</li>
      <li>Venture Capital Funding</li>
      <li>Merchant Funding</li>
      <li>Receivable/Purchase Order Funding</li>
    </ul>
  </section>

  <section class="card card--back-white">
    <div class="brand brand--centered brand--dark"><span class="brand__dot"></span>BrightHollow Capital Partners</div>
    <ul class="services services--dark">
      <li>Angel Investors/Angel Funds</li>
      <li>Seed/Start-up Investment</li>
      <li>Private Equity Funds</li>
      <li>Venture Capital Funding</li>
      <li>Merchant Funding</li>
      <li>Receivable/Purchase Order Funding</li>
    </ul>
  </section>

  <section class="card card--back-black">
    <div class="brand brand--centered brand--light"><span class="brand__dot"></span>BrightHollow Capital Partners</div>
    <ul class="services services--light">
      <li>Angel Investors/Angel Funds</li>
      <li>Seed/Start-up Investment</li>
      <li>Private Equity Funds</li>
      <li>Venture Capital Funding</li>
      <li>Merchant Funding</li>
      <li>Receivable/Purchase Order Funding</li>
    </ul>
  </section>

</body>
</html>
```